I need to refresh my meeting minutes pages (2 of them)

I have 2 pages that need to be modernized with a new look and feel. I have attached the 2 pages that need the refresh. I am okay with one page submissions as long as the winner is willing to add the second page before payment :-) Any questions please let me know. The logo on the page is not ours but a sample of what client may give us.

```html
<!DOCTYPE html>
<html lang="en">
<head>
<meta charset="utf-8">
<title>Regular Meeting Agenda</title>
<link rel="stylesheet" href="https://fonts.googleapis.com/css2?family=Figtree:wght@400;500;600;700&display=swap">
<style>
:root{
  --bg:#f7f7f7;
  --surface:#ffffff;
  --item:#f6f6f6;
  --line:#e4e4e4;
  --ink:#1c1c1c;
  --ink-soft:#3c3c3c;
  --muted:#7a7a7a;
  --accent:#0a84f5;
  --accent-ink:#ffffff;
}
*{box-sizing:border-box;margin:0;padding:0}
html,body{width:1200px;height:675px;overflow:hidden}
body{background:var(--bg);font-family:"Figtree",sans-serif;color:var(--ink);position:relative}
svg{display:block}
.site-header{position:absolute;left:0;top:0;width:1200px;height:61px;border-bottom:1px solid var(--line)}
.brand{position:absolute;left:18px;top:20px;font-size:16.5px;font-weight:600;letter-spacing:-.2px}
.powered{position:absolute;right:18px;top:17px;font-size:9.2px;color:var(--muted);line-height:15px}
.powered u{text-decoration:underline}
.side-nav{position:absolute;left:18px;top:82px;width:60px}
.nav-item{height:54px;margin-bottom:12px;display:flex;flex-direction:column;align-items:center;justify-content:center;gap:5px;font-size:8.5px;color:var(--muted);border-radius:5px}
.nav-item.active{background:var(--accent);color:var(--accent-ink)}
.meeting-list{position:absolute;left:96px;top:79px;width:300px;height:578px;background:var(--surface);border-radius:7px;overflow:hidden}
.search{height:38px;border-bottom:1px solid var(--line);display:flex;align-items:center;padding-left:12px;gap:11px;font-size:10.5px;color:#a8a8a8}
.group{height:36px;margin:0 12px;border-bottom:1px solid var(--line);display:flex;align-items:center;justify-content:space-between;font-size:9.5px;font-weight:700}
.group.open{border-bottom:none}
.items{padding:0 12px}
.item{height:45px;margin-bottom:2.3px;background:var(--item);border-radius:4px;padding:9px 0 0 36px;position:relative}
.item .date{font-size:11px;font-weight:600;line-height:14px}
.item .type{font-size:9.2px;color:var(--ink-soft);margin-top:2px}
.item.active{background:var(--accent);color:var(--accent-ink)}
.item.active .type{color:var(--accent-ink)}
.item .star{position:absolute;left:12px;top:16px}
.scrollbar{position:absolute;left:389px;top:119px;width:3px;height:180px;background:#dcdcdc;border-radius:2px}
.pager{position:absolute;left:432px;top:79px;width:71px;height:33px;border:1px solid var(--line);border-radius:4px;background:var(--surface);display:flex}
.pager span{flex:1;display:flex;align-items:center;justify-content:center}
.pager span+span{border-left:1px solid var(--line)}
.share{position:absolute;left:1146px;top:79px;width:36px;height:33px;border:1px solid var(--line);border-radius:4px;background:var(--surface);display:flex;align-items:center;justify-content:center}
.title{position:absolute;left:432px;top:135px;font-size:20.5px;font-weight:700;letter-spacing:-.2px}
.details{position:absolute;left:432px;top:182px;width:750px;height:337px;background:var(--surface);border-radius:7px;padding:0 18px}
.row{display:flex;align-items:center;gap:12px;border-bottom:1px solid var(--line);font-size:11.2px;line-height:13.5px;color:var(--ink)}
.row svg{flex:none}
.row-date{height:50px}
.row-place{height:77px}
.row-time{height:50px}
.row-info{height:64px}
.actions{display:flex;justify-content:center;gap:6px;margin-top:18px}
.action{height:59px;background:var(--item);border-radius:4px;display:flex;flex-direction:column;align-items:center;justify-content:center;gap:12px;font-size:9.3px;font-weight:500;color:var(--accent);padding:0 12px}
</style>
</head>
<body>
<header class="site-header">
  <div class="brand">ClientName</div>
  <div class="powered">Powered by:<br><u>MeetingDesk</u>® A Brightwell Brand, © 2002–2025</div>
</header>

<nav class="side-nav">
  <div class="nav-item"><svg width="16" height="16" viewBox="0 0 16 16" fill="none" stroke="#7a7a7a" stroke-width="1.1"><circle cx="8" cy="8" r="7"/><path d="M8 4.3l1.1 2.3 2.5.3-1.8 1.7.4 2.5L8 9.9l-2.2 1.2.4-2.5-1.8-1.7 2.5-.3z"/></svg>Featured</div>
  <div class="nav-item active"><svg width="16" height="16" viewBox="0 0 16 16" fill="none" stroke="#fff" stroke-width="1.1"><circle cx="8" cy="3" r="1.6"/><path d="M5.5 7.5h5M3 7.5h10v2H3zM4 9.5v5M12 9.5v5M5.5 12h5"/><circle cx="4.5" cy="6" r="1.1"/><circle cx="11.5" cy="6" r="1.1"/></svg>Meetings</div>
  <div class="nav-item"><svg width="16" height="16" viewBox="0 0 16 16" fill="none" stroke="#7a7a7a" stroke-width="1.1"><rect x="1.5" y="2.5" width="13" height="11" rx="1.5"/><path d="M1.5 6h13M5 1v3M11 1v3"/><circle cx="11" cy="11" r="2.6" fill="#f7f7f7"/><path d="M11 9.8V11l.8.6"/></svg>Agenda</div>
  <div class="nav-item"><svg width="16" height="16" viewBox="0 0 16 16" fill="none" stroke="#7a7a7a" stroke-width="1.1"><path d="M3 1.5h7l3 3v10H3z"/><circle cx="8" cy="9" r="2.6"/><path d="M8 7.8v1.2"/></svg>Policies</div>
</nav>

<aside class="meeting-list">
  <div class="search"><svg width="14" height="14" viewBox="0 0 14 14" fill="none" stroke="#1c1c1c" stroke-width="1.3"><circle cx="6" cy="6" r="4.6"/><path d="M9.4 9.4l3.4 3.4"/></svg>Search Meetings</div>
  <div class="group">FEATURED<svg width="10" height="6" viewBox="0 0 10 6" fill="none" stroke="#1c1c1c" stroke-width="1.3"><path d="M1 1l4 4 4-4"/></svg></div>
  <div class="group open">2025<svg width="10" height="6" viewBox="0 0 10 6" fill="none" stroke="#1c1c1c" stroke-width="1.3"><path d="M1 5l4-4 4 4"/></svg></div>
  <div class="items">
    <div class="item"><svg class="star" width="12" height="12" viewBox="0 0 12 12" fill="none" stroke="#1c1c1c" stroke-width="1.1"><path d="M6 1l1.5 3.2 3.4.4-2.5 2.3.7 3.4L6 8.6 2.9 10.3l.7-3.4L1.1 4.6l3.4-.4z"/></svg><div class="date">May 1, 2025 (Thu)</div><div class="type">Special Meeting Agenda</div></div>
    <div class="item active"><div class="date">Apr 24, 2025 (Thu)</div><div class="type">Regular Meeting Agenda</div></div>
    <div class="item"><div class="date">Apr 10, 2025 (Thu)</div><div class="type">Regular Meeting Agenda</div></div>
    <div class="item"><div class="date">Mar 20, 2025 (Thu)</div><div class="type">Regular Meeting Agenda</div></div>
    <div class="item"><div class="date">Mar 17, 2025 (Mon)</div><div class="type">Special Meeting Agenda</div></div>
    <div class="item"><div class="date">Mar 12, 2025 (Wed)</div><div class="type">Special Meeting Agenda</div></div>
    <div class="item"><div class="date">Mar 6, 2025 (Thu)</div><div class="type">Regular Meeting Agenda</div></div>
    <div class="item"><div class="date">Feb 26, 2025 (Wed)</div><div class="type">Special Meeting Agenda - Cancelled</div></div>
    <div class="item"><div class="date">Feb 20, 2025 (Thu)</div><div class="type">Regular Meeting Agenda</div></div>
    <div class="item"><div class="date">Feb 6, 2025 (Thu)</div><div class="type">Regular Meeting Agenda</div></div>
  </div>
</aside>
<div class="scrollbar"></div>

<div class="pager">
  <span><svg width="7" height="10" viewBox="0 0 7 10" fill="none" stroke="#1c1c1c" stroke-width="1.4"><path d="M5.5 1L1.5 5l4 4"/></svg></span>
  <span><svg width="7" height="10" viewBox="0 0 7 10" fill="none" stroke="#1c1c1c" stroke-width="1.4"><path d="M1.5 1l4 4-4 4"/></svg></span>
</div>
<div class="share"><svg width="13" height="13" viewBox="0 0 13 13" fill="none" stroke="#1c1c1c" stroke-width="1.2"><circle cx="10" cy="3" r="1.9"/><circle cx="3" cy="6.5" r="1.9"/><circle cx="10" cy="10" r="1.9"/><path d="M4.7 5.6l3.6-1.7M4.7 7.4l3.6 1.7"/></svg></div>

<h1 class="title">Regular Meeting Agenda</h1>

<section class="details">
  <div class="row row-date"><svg width="12" height="12" viewBox="0 0 12 12" fill="none" stroke="#1c1c1c" stroke-width="1.1"><rect x="1" y="1.8" width="10" height="9" rx="1"/><path d="M1 4.5h10M3.5 .5v2.5M8.5 .5v2.5"/></svg>Thursday, April 24, 2025</div>
  <div class="row row-place"><svg width="12" height="12" viewBox="0 0 12 12" fill="none" stroke="#1c1c1c" stroke-width="1.1"><path d="M1.5 11.5V1h6v10.5M7.5 4.5h3v7M.5 11.5h11M3.3 3h1M3.3 5h1M3.3 7h1M5.5 3h.1M5.5 5h.1M5.5 7h.1"/></svg><div>Westfield High School Media Center<br>1400 North Maple Grove Road<br>Lakeview, Ohio 44010</div></div>
  <div class="row row-time"><svg width="12" height="12" viewBox="0 0 12 12" fill="none" stroke="#1c1c1c" stroke-width="1.1"><circle cx="6" cy="6" r="3.3"/><path d="M4.2 3.2L4.6 .6h2.8l.4 2.6M4.2 8.8l.4 2.6h2.8l.4-2.6M6 4.5V6l1 .7"/></svg>6:00 P.M.</div>
  <div class="row row-info"><svg width="12" height="12" viewBox="0 0 12 12" fill="none" stroke="#1c1c1c" stroke-width="1.1"><circle cx="6" cy="6" r="5.3"/><path d="M6 5.3v3.4M6 3.3v.3"/></svg><div>This meeting is a meeting of the Board of Education in public for the purpose of conducting the District's business. There is a time for public participation during the meeting as indicated in the agenda.</div></div>
  <div class="actions">
    <div class="action"><svg width="13" height="11" viewBox="0 0 13 11" fill="none" stroke="#1c1c1c" stroke-width="1.1"><path d="M4 1.5h8.5M4 4.2h8.5M4 6.9h8.5M4 9.6h8.5M.8 1.5h.9M.8 4.2h.9M.8 6.9h.9M.8 9.6h.9"/></svg>View the Agenda</div>
    <div class="action"><svg width="11" height="13" viewBox="0 0 11 13" fill="none" stroke="#1c1c1c" stroke-width="1.1"><path d="M1 .8h6.2L10 3.6v8.6H1z"/><path d="M5.5 4v5M3.6 7.2l1.9 1.9 1.9-1.9M3.5 10.4h4"/></svg>Download Agenda as PDF</div>
    <div class="action"><svg width="13" height="12" viewBox="0 0 13 12" fill="none" stroke="#1c1c1c" stroke-width="1.1"><path d="M3.2 4V.8h6.6V4M3.2 9H1V4h11v5H9.8M3.2 7h6.6v4.3H3.2z"/></svg>Print the Agenda</div>
  </div>
</section>
</body>
</html>
```